OTU Consulting Firm needs artwork for foyer

We are looking for a piece of artwork for our foyer entrance. It will be displayed on the white wall above the two armchairs.

The piece could be meaningful to our organisation, but also could be of an abstract nature. We want the artwork to be striking/interesting as it is displayed in the foyer. The artwork would be printed on a landscape canvas print with dimensions 76 cm x 152 cm.

Please see attached word document "Velm Studio" for all specifications.

Target Market(s)

Industry/Entity Type

Consulting

Requirements
Must have
• Please see attached word document "Velm Studio" for all specifications.
Nice to have
Should not have

```html
<!DOCTYPE html>
<html lang="en">
<head>
<meta charset="utf-8">
<title>Foyer Artwork – Values Diagram</title>
<link rel="stylesheet" href="https://fonts.googleapis.com/css2?family=Montserrat:wght@700&display=swap">
<style>
  :root {
    --bg: #ffffff;
    --frame: #0a7dbf;
    --link: #55b6e6;
    --deep: #0a7dbf;
    --sky: #55b6e6;
    --teal: #05a5c5;
    --aqua: #20adc0;
    --label: #ffffff;
  }
  html, body { margin: 0; padding: 0; overflow: hidden; background: var(--bg); }
  .artwork {
    position: relative;
    width: 1200px;
    height: 900px;
    background: var(--bg);
    font-family: "Montserrat", sans-serif;
    overflow: hidden;
  }
  .connectors { position: absolute; inset: 0; }
  .value {
    position: absolute;
    width: 130px;
    height: 62px;
    border-radius: 10px;
    display: flex;
    align-items: center;
    justify-content: center;
    text-align: center;
    color: var(--label);
    font-size: 11px;
    font-weight: 700;
    line-height: 1.3;
    text-transform: uppercase;
    letter-spacing: 0.01em;
    box-sizing: border-box;
    padding: 0 8px;
  }
  .value--deep { background: var(--deep); }
  .value--sky { background: var(--sky); }
  .value--teal { background: var(--teal); }
  .value--aqua { background: var(--aqua); }
  .value--lead { font-size: 13.5px; }
</style>
</head>
<body>
<main class="artwork">
  <svg class="connectors" width="1200" height="900" viewBox="0 0 1200 900" aria-hidden="true">
    <rect x="118" y="178" width="965" height="482" rx="68" fill="none" stroke="var(--frame)" stroke-width="10"/>
    <g fill="none" stroke="var(--link)" stroke-width="10">
      <line x1="583" y1="262" x2="601" y2="262"/>
      <line x1="741" y1="270" x2="776" y2="283"/>
      <line x1="408" y1="288" x2="443" y2="270"/>
      <path d="M272 334 Q245 350 228 374"/>
      <path d="M902 338 Q930 352 950 376"/>
      <line x1="296" y1="409" x2="399" y2="410"/>
      <line x1="540" y1="411" x2="643" y2="412"/>
      <line x1="785" y1="412" x2="889" y2="413"/>
      <path d="M226 448 Q240 485 270 500"/>
      <path d="M956 448 Q942 480 912 496"/>
      <line x1="378" y1="556" x2="443" y2="573"/>
      <line x1="583" y1="579" x2="601" y2="579"/>
      <line x1="742" y1="572" x2="805" y2="556"/>
    </g>
  </svg>

  <div class="value value--teal" style="left:447px;top:227px">Quality and Excellence</div>
  <div class="value value--sky" style="left:607px;top:227px">Development and Growth</div>
  <div class="value value--deep value--lead" style="left:781px;top:272px">Client Focus</div>
  <div class="value value--sky" style="left:274px;top:275px">Positive and Supportive</div>
  <div class="value value--teal" style="left:160px;top:379px">Integrity and Accountability</div>
  <div class="value value--deep" style="left:404px;top:379px">Collaboration</div>
  <div class="value value--sky" style="left:649px;top:379px">Responsive</div>
  <div class="value value--sky" style="left:893px;top:379px">Administration</div>
  <div class="value value--aqua" style="left:274px;top:488px">Nimble</div>
  <div class="value value--teal" style="left:781px;top:488px">Consulting</div>
  <div class="value value--deep" style="left:447px;top:547px">Innovation</div>
  <div class="value value--aqua" style="left:607px;top:547px">Evaluation</div>
</main>
</body>
</html>
```